I'm an Executive Coach. I need a cover for a leadership book.

Title: Quiet Compass Wide Horizon Guidance from the Center of the Spirit. The focus in my work "Soul Woven Purpose" I use a lot of fire and heart-centered frame work and imagery. The book should have a leadership presence with an inspirational feel. The purpose is to invite really smart leaders to pay attention and to lead from their heart so they can have great impact in the work they do and the lives they live. priyalangford.example to see site branding, colors. Author: Priya Langford

Target Market(s)

The audience is those lead others from the manager level to the executive level and entrepreneurs starting and leading their own companies They are usually trailblazers, care about connecting with people as they lead. The big message is being confifent to lead ftom values, intention and from what matters most.

Industry/Entity Type

Executive coaching

Font styles to use
Serif

Requirements
Must have
• Lighter feel. Perhaps avoid a total black background.
Nice to have
• While it is a leadership book, i would like it to feel creative and inviting not authoritative.
Should not have
• Dark colors as the main color

```html
<!DOCTYPE html>
<html lang="en">
<head>
<meta charset="utf-8">
<title>Quiet Compass Wide Horizon — Priya Langford</title>
<link rel="stylesheet" href="https://fonts.googleapis.com/css2?family=Roboto+Condensed:wght@800;900&family=Cormorant+Garamond:wght@500;600&family=EB+Garamond:wght@500&display=swap">
<style>
  :root {
    --backdrop: #eee4d8;
    --cover: #fbf6ef;
    --ember-red: #a41d20;
    --ink-light: #fbf6ef;
    --warm-grey: #5a4f49;
    --frame-glow: #b0181c;
  }
  html, body {
    margin: 0;
    padding: 0;
    width: 1200px;
    height: 1200px;
    overflow: hidden;
    background: var(--backdrop);
  }
  .canvas {
    display: block;
    width: 1200px;
    height: 1200px;
  }
  .title-line {
    font-family: "Roboto Condensed", "Arial Narrow", sans-serif;
    font-weight: 900;
    fill: var(--ember-red);
  }
  .title-line--boxed { fill: var(--ink-light); }
  .subtitle {
    font-family: "Cormorant Garamond", Georgia, serif;
    font-weight: 600;
    font-size: 18px;
    letter-spacing: 3.4px;
    fill: var(--warm-grey);
  }
  .author {
    font-family: "EB Garamond", Georgia, serif;
    font-weight: 500;
    font-size: 34px;
    letter-spacing: 1.5px;
    fill: var(--warm-grey);
  }
  .rule { stroke: var(--warm-grey); stroke-width: 1.2; }
</style>
</head>
<body>
<svg class="canvas" viewBox="0 0 1200 1200" xmlns="http://www.w3.org/2000/svg">
  <defs>
    <radialGradient id="ember-glow" cx="50%" cy="48%" r="55%">
      <stop offset="0%" stop-color="#e0575a"/>
      <stop offset="35%" stop-color="#f4a040"/>
      <stop offset="62%" stop-color="#c8322f"/>
      <stop offset="100%" stop-color="#8e1c1e"/>
    </radialGradient>
    <filter id="frame-blur" x="-5%" y="-5%" width="110%" height="110%">
      <feGaussianBlur stdDeviation="2"/>
    </filter>
    <filter id="hole-shadow" x="-20%" y="-20%" width="140%" height="140%">
      <feGaussianBlur stdDeviation="16"/>
    </filter>
  </defs>

  <g class="book-cover">
    <rect x="279" y="124" width="643" height="952" fill="none" stroke="var(--frame-glow)" stroke-width="3" opacity="0.6" filter="url(#frame-blur)"/>
    <rect x="279" y="124" width="643" height="952" fill="var(--cover)" stroke="var(--frame-glow)" stroke-width="1.2"/>

    <g class="title-block">
      <text class="title-line" x="393" y="255" font-size="80" textLength="412" lengthAdjust="spacingAndGlyphs">QUIET COMPASS</text>
      <rect x="396" y="262" width="410" height="54" fill="var(--ember-red)"/>
      <text class="title-line title-line--boxed" x="402" y="310" font-size="62" textLength="398" lengthAdjust="spacingAndGlyphs">WIDE HORIZON</text>
      <text class="title-line" x="393" y="371" font-size="66" textLength="412" lengthAdjust="spacingAndGlyphs">PERSONAL &amp;</text>

      <line class="rule" x1="395" y1="381" x2="805" y2="381"/>
      <text class="subtitle" x="600" y="401" text-anchor="middle" textLength="404" lengthAdjust="spacing">PROFESSIONAL GUIDANCE FROM</text>
      <text class="subtitle" x="600" y="420" text-anchor="middle" textLength="372" lengthAdjust="spacing">THE CENTER OF THE SPIRIT</text>
      <line class="rule" x1="395" y1="426" x2="805" y2="426"/>
    </g>

    <g class="heart-window">
      <polygon points="611,470 845,696 605,920 380,698" fill="#7a5a4c" opacity="0.3" filter="url(#hole-shadow)"/>
      <polygon points="611,510 813,696 606,876 407,698" fill="url(#ember-glow)" role="img" aria-label="Glowing heart of flame seen through torn paper opening"/>
    </g>

    <text class="author" x="605" y="1012" text-anchor="middle">Priya Langford</text>
  </g>
</svg>
</body>
</html>
```